Commercial Business Card - stand out, clean, simple, unique.

commercial real estate group located in Texas. Called 4 Ridges Real Estate. We want a unique yet clean and professional card. On one side I would like the 4R to be by itself or to look as unique or tasteful as possible. We have the logo in white, black, and color in case a black background or something similar looks best on one side. We need a space for our name, email, cell. website. And possibly room for a phrase or city.

Contact Information for Business Card

Name, Title, Email, Phone Number, website

```html
<!DOCTYPE html>
<html lang="en">
<head>
<meta charset="utf-8">
<title>4 Ridges Real Estate – Business Card</title>
<link href="https://fonts.googleapis.com/css2?family=Cinzel:wght@500&family=Roboto:wght@400;500&display=swap" rel="stylesheet">
<style>
  :root {
    --backdrop: #2b2b2b;
    --navy: #15307a;
    --navy-deep: #0d1f5c;
    --navy-light: #1f3f95;
    --orange: #e0782f;
    --ink: #3a3a3a;
    --rule: #5a5a5a;
    --paper: #ffffff;
  }
  * { box-sizing: border-box; margin: 0; padding: 0; }
  html, body { width: 1200px; height: 960px; overflow: hidden; }
  body {
    background: var(--backdrop);
    font-family: "Roboto", sans-serif;
    position: relative;
  }
  .card {
    position: absolute;
    width: 640px;
    height: 366px;
    box-shadow: 0 12px 30px rgba(0,0,0,.45);
  }
  /* Front */
  .card-front {
    left: 280px; top: 64px;
    background: radial-gradient(ellipse at 50% 35%, var(--navy-light) 0%, var(--navy) 45%, var(--navy-deep) 100%);
    color: var(--paper);
    text-align: center;
  }
  .front-monogram {
    position: absolute;
    left: 0; right: 0; top: 70px;
    font-family: "Roboto", sans-serif;
    font-weight: 500;
    font-size: 150px;
    line-height: 1;
    letter-spacing: 4px;
  }
  .front-tagline {
    position: absolute;
    left: 0; right: 0; top: 290px;
    font-size: 15px;
    letter-spacing: .5px;
  }
  /* Back */
  .card-back {
    left: 280px; top: 520px;
    background: var(--paper);
    overflow: hidden;
  }
  .brand {
    position: absolute;
    top: 40px; right: 58px;
    display: flex;
    align-items: center;
    gap: 14px;
    color: var(--navy);
  }
  .brand-mark {
    font-weight: 500;
    font-size: 48px;
    line-height: 1;
  }
  .brand-divider {
    width: 1px; height: 58px;
    background: var(--navy);
  }
  .brand-name {
    font-weight: 500;
    font-size: 22px;
    line-height: 1.15;
    text-transform: uppercase;
    letter-spacing: 1px;
  }
  .header-rule {
    position: absolute;
    left: 300px; right: 44px; top: 128px;
    height: 1px; background: var(--rule);
  }
  .person {
    position: absolute;
    left: 40px; top: 186px;
  }
  .person-name {
    font-family: "Cinzel", serif;
    font-weight: 500;
    font-size: 27px;
    color: var(--navy);
    letter-spacing: 1px;
  }
  .person-title {
    font-size: 17px;
    color: var(--orange);
    font-weight: 500;
    margin-top: 2px;
  }
  .contact-rule {
    position: absolute;
    left: 40px; right: 190px; top: 258px;
    height: 1px; background: var(--rule);
  }
  .contacts {
    position: absolute;
    left: 40px; top: 268px;
    list-style: none;
    font-size: 16px;
    color: var(--ink);
  }
  .contacts li {
    display: flex; align-items: center; gap: 10px;
    height: 22px;
  }
  .contacts svg { width: 14px; height: 14px; fill: var(--navy); flex: none; }
  .website {
    position: absolute;
    right: 44px; top: 214px;
    font-size: 16px;
    letter-spacing: 1.5px;
    color: var(--ink);
  }
  .bottom-band {
    position: absolute;
    left: 0; right: 0; bottom: 0; height: 14px;
    background: var(--navy);
    border-top: 3px solid var(--orange);
  }
</style>
</head>
<body>
  <section class="card card-front">
    <div class="front-monogram">4R</div>
    <p class="front-tagline">I will find your ideal home</p>
  </section>

  <section class="card card-back">
    <div class="brand">
      <span class="brand-mark">4R</span>
      <span class="brand-divider"></span>
      <span class="brand-name">4 Ridges<br>Real Estate</span>
    </div>
    <div class="header-rule"></div>

    <div class="person">
      <h1 class="person-name">DANIEL REYES</h1>
      <p class="person-title">CEO/FOUNDER</p>
    </div>
    <div class="contact-rule"></div>

    <ul class="contacts">
      <li>
        <svg viewBox="0 0 24 24" aria-hidden="true"><path d="M6.6 10.8a15 15 0 0 0 6.6 6.6l2.2-2.2c.3-.3.7-.4 1-.2 1.1.4 2.3.6 3.6.6.6 0 1 .4 1 1V20c0 .6-.4 1-1 1A17 17 0 0 1 3 4c0-.6.4-1 1-1h3.5c.6 0 1 .4 1 1 0 1.3.2 2.5.6 3.6.1.3 0 .7-.2 1z"/></svg>
        512 555 0148
      </li>
      <li>
        <svg viewBox="0 0 24 24" aria-hidden="true"><path d="M7 2h10a2 2 0 0 1 2 2v16a2 2 0 0 1-2 2H7a2 2 0 0 1-2-2V4a2 2 0 0 1 2-2zm0 3v13h10V5zm5 14.2a1 1 0 1 0 0 .1z"/></svg>
        512 555 0193
      </li>
      <li>
        <svg viewBox="0 0 24 24" aria-hidden="true"><path d="M2 5h20v14H2zm2 2v.5l8 5 8-5V7zm0 2.8V17h16V9.8l-8 5z"/></svg>
        daniel@4ridges.com
      </li>
    </ul>

    <p class="website">www.4ridges.com</p>
    <div class="bottom-band"></div>
  </section>
</body>
</html>
```